Strand Wire Depot PureSnap LC Fiber Optic Cleaner

I'm looking for a unique package design of a long, rectangular box for a fiber optic cable cleaner. The design should be to the measurements of the package and should be on at least two of the sides, but can be on up to 6 sides, including the top and bottom. The measurements of the package are 7 1/4" long, by 1" wide and 1" deep. This is an item used in technology so the design should have that look and feel. The content for the package is below in the must haves section.

Target Market(s)

Tech market, primarily men - 25 to 60

Industry/Entity Type

Technology Equipment

Colors

Designer to choose colors to be used in the design.

Requirements
Must have
• Name must be on the packaging - PureSnap LC Fiber Optic Cleaner
• These must also be on the package:
• - Designed for LC/MU connections, 1.25mm ferules and adapters
• - Up to 800 cleanings for spotless results
• - Simple one-click action
• the StrandWireDepot logo (attached)
• - The UPC Code. attached.
Nice to have
• You can use any colors you want. I do want a clean design, the box is white, so not to much clutter.
Should not have
• Should not be whimsical or cartoon-like.

```html
<!DOCTYPE html>
<html lang="en">
<head>
<meta charset="utf-8">
<title>PureSnap LC Fiber Optic Cleaner – Package Panels</title>
<link href="https://fonts.googleapis.com/css2?family=Montserrat:ital,wght@0,400;0,500;0,600;0,700;1,500&display=swap" rel="stylesheet">
<style>
  :root {
    --brand-green: #3f9e3f;
    --paper: #ffffff;
    --stage: #e4e4e4;
    --ink: #333333;
    --photo-light: #eeeeee;
    --photo-mid: #cfcfcf;
  }
  * { box-sizing: border-box; margin: 0; padding: 0; }
  html, body { width: 1200px; height: 676px; overflow: hidden; }
  body {
    background: var(--stage);
    font-family: "Montserrat", sans-serif;
    color: var(--ink);
    position: relative;
  }
  .panel {
    position: absolute;
    left: 56px;
    width: 1088px;
    height: 150px;
    background: var(--paper);
    overflow: hidden;
    box-shadow: 0 2px 8px rgba(0,0,0,.08);
  }
  .panel--front { top: 110px; }
  .panel--back { top: 390px; }
  .wave { position: absolute; inset: 0; width: 100%; height: 100%; }
  .wave path { fill: var(--brand-green); }

  /* front */
  .front-title {
    position: absolute; left: 26px; top: 16px;
    color: var(--paper); font-weight: 700; font-size: 21px; line-height: 1.05;
  }
  .front-features {
    position: absolute; left: 26px; top: 66px;
    list-style: none; color: var(--paper);
    font-size: 7.5px; font-weight: 600; text-transform: uppercase;
    letter-spacing: .06em; line-height: 1.45;
  }
  .product-photo {
    position: absolute; right: 30px; top: 10px; width: 360px; height: 46px;
    border-radius: 23px;
    background: linear-gradient(90deg, var(--photo-mid), var(--photo-light) 40%, var(--brand-green) 70%, var(--photo-light));
  }
  .detail-photos {
    position: absolute; left: 480px; top: 62px; display: flex; gap: 24px;
  }
  .detail-photo {
    width: 50px; height: 50px; border-radius: 50%;
    border: 1.5px solid var(--brand-green);
    background: radial-gradient(circle, var(--photo-light), var(--photo-mid));
  }
  .front-tagline {
    position: absolute; left: 200px; bottom: 12px;
    color: var(--brand-green); font-style: italic; font-weight: 500; font-size: 12.5px;
  }

  /* back */
  .brand-name {
    position: absolute; left: 26px; top: 14px;
    color: var(--brand-green); font-weight: 600; font-size: 13px;
  }
  .back-intro {
    position: absolute; left: 26px; top: 40px; width: 330px;
    font-size: 8.6px; line-height: 1.4; color: var(--ink);
  }
  .back-intro strong { color: var(--brand-green); font-weight: 600; }
  .back-photo {
    position: absolute; left: 380px; top: 12px; width: 300px; height: 40px; border-radius: 20px;
    background: linear-gradient(90deg, var(--photo-mid), var(--photo-light) 50%, var(--brand-green) 80%, var(--photo-light));
  }
  .back-usage {
    position: absolute; left: 380px; top: 66px; width: 320px;
    font-size: 8.6px; line-height: 1.4;
  }
  .back-band-title {
    position: absolute; right: 28px; bottom: 56px;
    color: var(--paper); font-weight: 700; font-size: 17px; line-height: 1.05; text-align: right;
  }
  .back-band-features {
    position: absolute; right: 28px; bottom: 14px; list-style: none; text-align: right;
    color: var(--paper); font-size: 6.5px; font-weight: 600; text-transform: uppercase;
    letter-spacing: .06em; line-height: 1.45;
  }
</style>
</head>
<body>

<section class="panel panel--front" aria-label="Front panel">
  <svg class="wave" viewBox="0 0 1088 150" preserveAspectRatio="none" aria-hidden="true">
    <path d="M0 0 H470 C470 30 440 40 410 40 C380 40 370 70 370 80 C370 100 330 108 280 108 C200 108 120 120 0 150 Z"/>
  </svg>
  <h1 class="front-title">PureSnap LC<br>Fiber Optic Cleaner</h1>
  <ul class="front-features">
    <li>Designed for LC/MU connections, 1.25mm ferules and adapters</li>
    <li>Up to 800 cleanings for spotless results</li>
    <li>Simple one-click action</li>
  </ul>
  <div class="product-photo" role="img" aria-label="Photo of the white and green cleaning pen"></div>
  <div class="detail-photos">
    <div class="detail-photo" role="img" aria-label="Close-up of connector end face"></div>
    <div class="detail-photo" role="img" aria-label="Close-up of cleaning tape"></div>
    <div class="detail-photo" role="img" aria-label="Adapter cap detail"></div>
    <div class="detail-photo" role="img" aria-label="Extendable tip detail"></div>
  </div>
  <p class="front-tagline">Single action system SC Fiber Optic Cleaner with 2.5mm adapter cap for cleaning ST and FC mounted fiber connectors.</p>
</section>

<section class="panel panel--back" aria-label="Back panel">
  <svg class="wave" viewBox="0 0 1088 150" preserveAspectRatio="none" aria-hidden="true">
    <path d="M1088 150 H700 C700 130 720 118 745 118 C775 118 790 105 790 90 C790 70 830 62 880 62 C960 62 1020 55 1088 20 Z"/>
  </svg>
  <p class="brand-name">Strand Wire Depot</p>
  <p class="back-intro"><strong>Try our easy-to-use, Pure Snap, SC Fiber Optic Cleaner on your SC, ST and FC adapter mounted fiber connections (Both APC and UPC).</strong> Each of these disposable fiber cleaning pens come with enough densely stranded micro fiber to clean 800 connections. This pen is a must for any fiber optic network technician, installer, engineer or IT manager.</p>
  <div class="back-photo" role="img" aria-label="Photo of the cleaning pen"></div>
  <p class="back-usage">With an easy pushing motion, the micro fiber cleaning tip rotates a 180 degrees to effectively wipe clean a variety of contaminates. And with an extendable tip, you can easily reach recessed fiber connectors. Just push until you hear the 'Click', and your cable is connection is clean.</p>
  <h2 class="back-band-title">PureSnap LC<br>Fiber Optic Cleaner</h2>
  <ul class="back-band-features">
    <li>Designed for LC/MU connections, 1.25mm ferules and adapters</li>
    <li>Up to 800 cleanings for spotless results</li>
    <li>Simple one-click action</li>
  </ul>
</section>

</body>
</html>
```